IG ad to attract older men for better health #1

I want a bold headline Instagram Ad that coordinate with my website design with a racy sexy woman to attract men 45yrs old plus. See Two samples attached

Target Market(s)

Men 45 years old and older

Industry/Entity Type

Health And Wellness

Requirements
Must have
• eye catching appeal to men
Nice to have
• The copy to read
Kestrel61go is the headline at the top of the page. Then the copy reads...
"I want to seduce you to better health with a little T&A. Remove the excuses, provide ridiculously simple tips and advice to get you started on a path of lasting heath." Want more?

```html
<!DOCTYPE html>
<html lang="en">
<head>
<meta charset="utf-8">
<title>Kestrel61go — Instagram Ad</title>
<link rel="stylesheet" href="https://fonts.googleapis.com/css2?family=Black+Ops+One&family=Saira:wght@500;600&family=Montserrat:wght@800&display=swap">
<style>
  :root {
    --ink: #050505;
    --gym-dark: #0d0d0d;
    --gym-mid: #2a2a2a;
    --headline-yellow: #ffe600;
    --text-white: #ffffff;
    --skin-light: #e7c3a8;
    --skin-warm: #c58e6c;
  }
  * { margin: 0; padding: 0; box-sizing: border-box; }
  html, body { width: 1200px; height: 1200px; overflow: hidden; background: var(--ink); }
  .ad {
    position: relative;
    width: 1200px;
    height: 1200px;
    overflow: hidden;
    background: var(--ink);
  }
  .gym-backdrop {
    position: absolute;
    inset: 0;
    background: radial-gradient(ellipse at 55% 55%, var(--gym-mid) 0%, var(--gym-dark) 55%, var(--ink) 100%);
  }
  .model {
    position: absolute;
  }
  .model--left {
    left: 0;
    top: 272px;
    width: 290px;
    height: 928px;
    background: linear-gradient(180deg, #d9b77a 0%, var(--skin-light) 35%, #9fd3e0 62%, var(--skin-light) 80%);
    border-radius: 0 140px 0 0;
  }
  .model--right {
    right: 0;
    top: 256px;
    width: 290px;
    height: 944px;
    background: linear-gradient(180deg, #2a1d17 0%, var(--skin-warm) 30%, #1a1a1a 55%, var(--skin-warm) 72%, #1a1a1a 92%);
    border-radius: 140px 0 0 0;
  }
  .headline {
    position: absolute;
    top: 122px;
    left: 0;
    width: 100%;
    text-align: center;
    font-family: "Black Ops One", system-ui, sans-serif;
    font-weight: 400;
    font-size: 104px;
    line-height: 1;
    color: var(--headline-yellow);
  }
  .subhead {
    position: absolute;
    top: 272px;
    left: 320px;
    width: 560px;
    text-align: center;
    font-family: "Saira", sans-serif;
    font-weight: 500;
    font-size: 36px;
    line-height: 44px;
    white-space: nowrap;
    color: var(--text-white);
  }
  .pitch {
    position: absolute;
    top: 402px;
    left: 310px;
    width: 580px;
    text-align: center;
    font-family: "Saira", sans-serif;
    font-weight: 500;
    font-size: 33px;
    line-height: 44px;
    white-space: nowrap;
    color: var(--text-white);
  }
  .cta {
    position: absolute;
    top: 898px;
    left: 458px;
    width: 281px;
    text-align: center;
    font-family: "Montserrat", sans-serif;
    font-weight: 800;
  }
  .cta__lead {
    display: block;
    font-size: 56px;
    line-height: 60px;
    color: var(--text-white);
  }
  .cta__action {
    display: block;
    margin-top: 4px;
    height: 67px;
    font-size: 54px;
    line-height: 67px;
    color: var(--ink);
    background: var(--headline-yellow);
  }
</style>
</head>
<body>
  <main class="ad">
    <div class="gym-backdrop" role="img" aria-label="Dark photo of a gym interior with treadmills and large windows"></div>
    <div class="model model--left" role="img" aria-label="Smiling blonde woman in a light blue bikini, hand on hip"></div>
    <div class="model model--right" role="img" aria-label="Dark-haired woman in a black ruffled bikini, hands on hips"></div>

    <h1 class="headline">Kestrel61go</h1>
    <p class="subhead">Out of shape and overweight</p>
    <p class="pitch">"I want to seduce you to<br>better health with a little T&amp;A.<br>Remove the excuses, provide<br>ridiculously simple tips<br>and advice to get you<br>started on a path<br>of lasting heath."</p>

    <div class="cta">
      <span class="cta__lead">WANT</span>
      <span class="cta__action">MORE?</span>
    </div>
  </main>
</body>
</html>
```